Harbor Mortgage Relief

Please help us give our website a remake or a FACELIFT. It is not very good but it says what we need it to say. But the design is terrible.
I would like our new design font and logo to be used as the theme.

I also want more photos on the site.

I also want consistency with the pages so they look clean.

We want the professionals to do this, let's see what you got!

Thank you!
Updates

Project Deadline Extended
Reason: I can understand you want to be paid. So I will commit to the fee but I want you to have time to make a KICK ASS website for me dudes! Thanks

HI!  Just wanted to say thanks for your time on these.  A lot are great.  However the firefighters have nothing to do with Foreclosure.  We are saving peoples homes from the bank taking them and selling them.   I LOVE the house photos and the families on the website.  That is the direction we like.  THanks.

THANK U ALL FOR THE WORK!   I like a few ending in the numbers: 147  733  693  536  620  478  727  508     I will go over them and choose one soon.  Thank you.   You will be paid shortly. 

Requirements
Must have
• Bright, Upbeat photos. Color scheme should be in order. We like icons on the bottom. not just text.

```html
<!DOCTYPE html>
<html lang="en">
<head>
<meta charset="utf-8">
<title>Harbor Mortgage Relief</title>
<link rel="stylesheet" href="https://fonts.googleapis.com/css2?family=Arimo:wght@400;700&family=Cinzel:wght@400;700&family=Roboto+Condensed:wght@400;700&family=Tinos:ital,wght@0,400;1,400&display=swap">
<style>
:root{
  --red:#e8313a;
  --red-dark:#c9252d;
  --blue:#1b8fd8;
  --page:#e4e5e7;
  --white:#ffffff;
  --ink:#444548;
  --muted:#6a6b6e;
  --nav-top:#5b5c5f;
  --nav-bottom:#323336;
  --form-bg:rgba(58,70,92,.86);
  --footer-top:#0d4a85;
  --footer-bottom:#082a4d;
  --footer-link:#dce6f2;
  --footer-head:#5fb4f0;
  --line:#c9cacc;
}
*{box-sizing:border-box;margin:0;padding:0}
html,body{width:815px;height:1200px;overflow:hidden}
body{position:relative;background:var(--page);font-family:"Arimo",Arial,sans-serif;color:var(--ink)}
.abs{position:absolute}
.header-band{left:0;top:0;width:815px;height:147px;background:var(--white)}
.utility-tab{left:621px;top:0;width:88px;height:19px;background:#e6e6e7;font-size:8px;color:var(--muted);display:flex;align-items:center;justify-content:center;gap:4px}
.brand{left:116px;top:38px;display:flex;align-items:center;gap:10px}
.brand-mark{width:54px;height:54px;border-radius:50%;background:var(--red)}
.brand-name{font-family:"Arimo",Arial,sans-serif;font-weight:700;font-size:18px;line-height:18px;color:var(--red);text-transform:uppercase;width:150px}
.call{left:423px;top:63px;font-size:13px;color:var(--ink);font-family:"Arimo",Arial,sans-serif}
.phone{left:533px;top:50px;font-family:"Tinos",serif;font-size:32px;color:var(--blue)}
.main-nav{left:105px;top:105px;width:604px;height:31px;background:linear-gradient(var(--nav-top),var(--nav-bottom));display:flex;align-items:center;border-radius:2px}
.nav-home{width:73px;height:31px;display:flex;align-items:center;justify-content:center;border-right:1px solid #2a2b2d}
.nav-item{font-family:"Roboto Condensed",sans-serif;font-size:13px;color:#f1f1f1;padding:0 12px;height:31px;display:flex;align-items:center;border-right:1px solid #2a2b2d}
.search{position:absolute;left:473px;top:6px;width:121px;height:19px;background:var(--white);border-radius:2px;font-size:9px;color:#888;padding:4px 6px}
.search-btn{position:absolute;right:0;top:0;width:18px;height:19px;background:var(--red);display:flex;align-items:center;justify-content:center}
.hero-photo{left:105px;top:147px;width:605px;height:254px;background:linear-gradient(160deg,#2a6fc9 0%,#4c8ed6 45%,#7f6a58 80%,#3b4e3c 100%);border-radius:0 0 6px 6px}
.consult{left:510px;top:147px;width:200px;height:254px;background:var(--form-bg);border-radius:0 0 6px 0}
.consult-head{position:absolute;left:0;top:0;width:200px;height:36px;background:var(--red);color:var(--white);font-family:"Roboto Condensed",sans-serif;font-weight:700;font-size:15px;display:flex;align-items:center;justify-content:center}
.consult-note{position:absolute;left:16px;top:45px;width:180px;font-size:11px;line-height:13px;color:var(--white)}
.field{position:absolute;background:var(--white);border:1px solid #d5d6d8;border-radius:2px;font-size:8.5px;color:#7a7b7e;padding:6px 9px}
.field b{color:var(--red);font-weight:400}
.select-btn{position:absolute;right:3px;top:3px;width:16px;height:16px;background:var(--blue);border-radius:2px}
.send-request{position:absolute;left:16px;top:200px;width:172px;height:33px;background:linear-gradient(#6a6c70,#3d3f44);color:#a9d8f7;font-family:"Tinos",serif;font-size:18px;letter-spacing:1px;display:flex;align-items:center;justify-content:center;border-radius:2px}
.feature-photo{top:423px;height:90px}
.feature-text{top:532px;width:132px;font-size:9.5px;line-height:15.5px;color:var(--ink)}
.btn-red{height:25px;background:var(--red);color:var(--white);font-family:"Tinos",serif;font-size:12px;display:flex;align-items:center;justify-content:center;border-radius:1px}
.news-title{left:559px;top:419px;font-family:"Cinzel",serif;font-size:20px;color:var(--red)}
.news-rule{left:547px;top:443px;width:172px;height:1px;background:var(--line)}
.news-list{left:547px;top:450px;list-style:none;font-size:8.5px;color:var(--ink)}
.news-list li{height:16.8px;line-height:16.8px}
.news-list li::before{content:"»";color:var(--red);margin-right:5px}
.about-title{left:108px;top:657px;font-family:"Cinzel",serif;font-size:21px;color:var(--red);letter-spacing:.5px}
.about-copy{left:108px;top:684px;width:420px;font-size:12.4px;line-height:19.3px;letter-spacing:.4px;color:var(--ink)}
.about-copy em{font-style:normal;color:var(--red)}
.btn-light{background:linear-gradient(#fafafa,#e9e9ea);border:1px solid #cdcecf;color:var(--muted);font-family:"Tinos",serif;font-size:12px;display:flex;align-items:center;justify-content:center;border-radius:2px}
.testimonial{left:108px;top:821px;width:403px;height:103px;background:var(--white);border:1px solid #d7d8da;border-radius:3px}
.testimonial-title{position:absolute;left:0;width:100%;top:12px;text-align:center;font-family:"Cinzel",serif;font-size:20px;color:var(--red);letter-spacing:1px}
.quote-mark{position:absolute;font-family:"Tinos",serif;font-size:38px;color:#8d8e91;line-height:1}
.quote-text{position:absolute;left:43px;top:45px;width:350px;font-family:"Tinos",serif;font-style:italic;font-size:12px;line-height:18px;color:var(--muted)}
.quote-by{position:absolute;left:43px;top:85px;font-size:8.5px;color:var(--muted)}
.contact-card{left:541px;top:650px;width:177px;height:274px;background:#eeeff0;border:1px solid #d3d4d6;border-radius:3px}
.contact-inner{position:absolute;left:4px;top:4px;right:4px;bottom:4px;border:1px solid #d9dadc;border-radius:2px}
.contact-title{position:absolute;left:0;width:100%;top:18px;text-align:center;font-family:"Cinzel",serif;font-size:21px;color:#5a5b5e}
.footer{left:0;top:985px;width:815px;height:215px;background:radial-gradient(ellipse at 50% 0%,var(--footer-top),var(--footer-bottom) 80%)}
.footer-col{top:1027px;font-size:7.5px;line-height:13px;color:var(--footer-link)}
.footer-col h3{font-size:12.5px;color:var(--footer-head);font-weight:700;margin-bottom:3px;line-height:15px}
.news-head{left:379px;top:1028px;font-size:12.5px;font-weight:700;color:var(--white)}
.news-input{left:377px;top:1054px;width:150px;height:23px;background:var(--white);border-radius:3px;font-size:9px;color:#777;padding:6px 9px}
.subscribe{left:535px;top:1053px;width:75px;height:25px;background:var(--red);border-radius:3px;color:var(--white);font-weight:700;font-size:11px;display:flex;align-items:center;justify-content:center}
.social{top:1055px;width:20px;height:21px;background:#e3e4e6;border-radius:3px}
.footer-rule{left:0;top:1128px;width:815px;height:1px;background:rgba(255,255,255,.12)}
.legal{left:119px;top:1150px;font-size:7.5px;color:var(--footer-link)}
.copyright{left:119px;top:1162px;font-size:7.5px;color:#4da6e8}
</style>
</head>
<body>
<div class="abs header-band"></div>
<div class="abs utility-tab"><span>Login</span><span>|</span><span>Contacts</span></div>

<div class="abs brand">
  <div class="brand-mark"></div>
  <div class="brand-name">Harbor Mortgage Relief</div>
</div>
<div class="abs call">Call Toll-Free Now</div>
<div class="abs phone">877-555-0142</div>

<nav class="abs main-nav">
  <div class="nav-home">
    <svg width="16" height="14" viewBox="0 0 16 14"><path d="M8 1 1 7h2v6h4V9h2v4h4V7h2z" fill="#fff"/></svg>
  </div>
  <div class="nav-item">ABOUT US</div>
  <div class="nav-item">SERVICES</div>
  <div class="nav-item">FINANCING OPTIONS</div>
  <div class="nav-item">CONTACT US</div>
  <div class="search">Search...
    <div class="search-btn"><svg width="10" height="10" viewBox="0 0 10 10"><circle cx="4" cy="4" r="3" fill="none" stroke="#fff" stroke-width="1.4"/><path d="M6 6 9 9" stroke="#fff" stroke-width="1.6"/></svg></div>
  </div>
</nav>

<div class="abs hero-photo" role="img" aria-label="Smiling family of five outdoors under a blue sky in front of their house"></div>

<form class="abs consult">
  <div class="consult-head">GET A FREE CONSULTATION</div>
  <p class="consult-note">Please fill out this form, and we´ll call you as soon as possible.</p>
  <div class="field" style="left:16px;top:82px;width:172px;height:22px">Name <b>*</b></div>
  <div class="field" style="left:16px;top:109px;width:172px;height:22px">Email <b>*</b></div>
  <div class="field" style="left:16px;top:136px;width:172px;height:22px">Phone <b>*</b></div>
  <div class="field" style="left:16px;top:164px;width:172px;height:22px">State property is <b>*</b>
    <div class="select-btn"><svg width="16" height="16" viewBox="0 0 16 16"><path d="M4 6l4 4 4-4" fill="none" stroke="#fff" stroke-width="1.8"/></svg></div>
  </div>
  <div class="send-request">SEND REQUEST</div>
</form>

<div class="abs feature-photo" style="left:105px;width:136px;background:linear-gradient(#9cc4e8,#d9d2c0 55%,#4f9a3a 75%)" role="img" aria-label="Family standing on the lawn before a yellow house"></div>
<div class="abs feature-photo" style="left:247px;width:135px;background:linear-gradient(#4a95d8,#8cc0ec 50%,#eef2f6)" role="img" aria-label="Father and children laughing together on a sunny day"></div>
<div class="abs feature-photo" style="left:387px;width:129px;background:linear-gradient(#9ab7cf,#6f7a5a 45%,#5aa23c 75%)" role="img" aria-label="Parents and child playing on the grass outside their home"></div>

<p class="abs feature-text" style="left:108px">Nulla venenatis. In pede mi, aliquet sit amet, euismod in, auctor ut, ligula.</p>
<p class="abs feature-text" style="left:249px">Nulla venenatis. In pede mi, aliquet sit amet, euismod in, auctor ut, ligula.</p>
<p class="abs feature-text" style="left:392px">Nulla venenatis. In pede mi, aliquet sit amet, euismod in, auctor ut, ligula.</p>

<div class="abs btn-red" style="left:108px;top:595px;width:107px">LEARN MORE</div>
<div class="abs btn-red" style="left:249px;top:595px;width:107px">LEARN MORE</div>
<div class="abs btn-red" style="left:391px;top:595px;width:107px">LEARN MORE</div>

<h2 class="abs news-title">Latest News</h2>
<div class="abs news-rule"></div>
<ul class="abs news-list">
  <li>Aliquam dapibus tincidunt metus ..</li>
  <li>Praesent justo dolor sagittis euismod..</li>
  <li>Vestibulum sed ante</li>
  <li>Donec sagittis euismod purus</li>
  <li>Praesent justo dolor sagittis ...</li>
  <li>Aliquam dapibus tincidunt metus ..</li>
  <li>Praesent justo dolor sagittis euismod..</li>
  <li>Vestibulum sed ante</li>
</ul>
<div class="abs btn-red" style="left:556px;top:595px;width:107px">See More&nbsp;
  <svg width="12" height="10" viewBox="0 0 12 10"><path d="M1 1l4 4-4 4M6 1l4 4-4 4" fill="none" stroke="#fff" stroke-width="1.8"/></svg></div>

<h2 class="abs about-title">About Harbor Mortgage Relief</h2>
<p class="abs about-copy">Aliquam congue fermentum nisl. Mauris accumsan nulla vel diam. Sed in lacus ut enim <em>adipiscing</em> aliquet. Nulla venenatis. In pede mi, aliquet sit amet, euismod in, auctor ut, ligula. Aliquam dapibus tincidunt metus. Praesent justo dolor.</p>
<div class="abs btn-light" style="left:108px;top:773px;width:81px;height:27px">Read More</div>

<section class="abs testimonial">
  <h2 class="testimonial-title">TESTIMONIAL</h2>
  <span class="quote-mark" style="left:17px;top:32px">“</span>
  <p class="quote-text">Nulla venenatis. In pede mi, aliquet sit amet, euismod in, auctor ut, ligula. Aliquam dapibus tincidunt metus. Praesent justo dolor.</p>
  <span class="quote-mark" style="left:365px;top:65px">”</span>
  <p class="quote-by">--Daniel Ward Home Owner, NH</p>
</section>

<form class="abs contact-card">
  <div class="contact-inner"></div>
  <h2 class="contact-title">Contact Us</h2>
  <div class="field" style="left:22px;top:55px;width:135px;height:24px">Name <b>*</b></div>
  <div class="field" style="left:22px;top:84px;width:135px;height:24px">Emai <b>*</b></div>
  <div class="field" style="left:22px;top:114px;width:135px;height:111px">Message <b>*</b></div>
  <div class="abs btn-light" style="left:93px;top:235px;width:62px;height:23px">SEND</div>
</form>

<footer class="abs footer"></footer>
<div class="abs footer-col" style="left:119px"><h3>About Us</h3>Company Info<br>Our Services<br>Clients<br>Partners</div>
<div class="abs footer-col" style="left:218px"><h3>Advice</h3>Sign up<br>Forums<br>Promotion<br>Career</div>
<div class="abs footer-col" style="left:303px"><h3>Join In</h3>FAQs<br>Solutions<br>Sitemap<br>Contacts</div>
<div class="abs news-head">Join our Newsletter</div>
<div class="abs news-input">Email Address:</div>
<div class="abs subscribe">Subscribe</div>
<div class="abs social" style="left:642px"></div>
<div class="abs social" style="left:665px"></div>
<div class="abs social" style="left:689px"></div>
<div class="abs footer-rule"></div>
<p class="abs legal">Disclaimer &amp; Terms &amp; Conditions &nbsp;|&nbsp; Privacy Policy &nbsp;|&nbsp; Advertise With Us &nbsp;|&nbsp; Contact Us</p>
<p class="abs copyright">Harbor Mortgage Relief &nbsp;© 2012. &nbsp;All Rights Reserved</p>
</body>
</html>
```